Heron Freightways LLC needs a web desigh ASAP!

We need a fully functioning web site for our trucking company!
we currently have our domain and logo.
Attached you will find our logo files and word documents with info we would like to include in our web page. (Navigation Tabs and dropdown menu)
Our domain is heronfreightways.net (from webnestly)
Our Chatterbook page is Heron Freightways LLC. You can find pictures and a little bit about our company.
our original logo is the one with bull on the left side.
Our trucking company is based in south Texas, but travel within the USA and Canada.

Target Market(s)

Logistic
Refrigerated Fleet Clients
Transportation
Trucking companies

Industry/Entity Type

Trucking Company

Coding

Coded - Design and coding required

Number of Pages Required

1 page

Font styles to use
Sans Serif

Colors
f04a51
3277b5
ffffff

Requirements
Must have
• our main email contact is Info@heronfreightways.net
• we would like see the colors of our logo. it would be nice to have a truck with our logo in the background.
• We need a web site that we can manage on our own easily.
Nice to have
• roads, highways
• get a quote module
• our inspirational web pages are:
• www.marwickhaulage.com
• www.dorvelcargo.com
• we are open to use stock photos

```html
<!DOCTYPE html>
<html lang="en">
<head>
<meta charset="utf-8">
<title>Heron Freightways LLC</title>
<link rel="stylesheet" href="https://fonts.googleapis.com/css2?family=Roboto:wght@300;400;500;700&display=swap">
<style>
:root{
  --red:#c41f2b;
  --red-light:#ee7d86;
  --blue:#1d62a8;
  --blue-light:#3a9ae0;
  --navy:#0b2a5b;
  --nav-band:#1f64ab;
  --ink:#2b2b2b;
  --muted:#555;
  --white:#ffffff;
  --brand-red:#f04a51;
  --brand-blue:#3277b5;
}
*{box-sizing:border-box;margin:0;padding:0}
html,body{width:1200px;height:2423px;overflow:hidden}
body{font-family:"Roboto",Arial,sans-serif;background:var(--white);color:var(--ink);position:relative}
.abs{position:absolute}

/* header */
.site-header{position:absolute;left:0;top:0;width:1200px;height:110px}
.nav-band{position:absolute;left:0;top:36px;width:1200px;height:74px;background:linear-gradient(90deg,#1b5a9c,#2a78c0 50%,#1b5a9c)}
.utility{position:absolute;top:8px;right:52px;display:flex;gap:16px;align-items:center;font-size:14px;color:#888}
.utility .item{display:flex;align-items:center;gap:6px}
.pill{font-size:13px;color:var(--white);padding:2px 8px;border-radius:3px;line-height:18px}
.pill.driver{background:#2a8ad6}
.pill.quote{background:#c01d24}
.pill.login{background:#0c2d5e}
.logo-box{position:absolute;left:53px;top:0;width:283px;height:94px;background:var(--white);border-radius:0 0 8px 8px;display:flex;align-items:center;justify-content:center;gap:10px;box-shadow:0 2px 4px rgba(0,0,0,.15)}
.logo-box .mark{width:22px;height:22px;border-radius:50%;background:var(--brand-blue)}
.logo-box .name{font-size:27px;font-weight:700;color:var(--brand-red);letter-spacing:.3px}
.main-nav{position:absolute;top:36px;right:52px;height:74px;display:flex;align-items:center;gap:37px}
.main-nav a{color:var(--white);text-decoration:none;font-size:17px;font-weight:500}

/* hero */
.hero{position:absolute;left:0;top:110px;width:1200px;height:480px;background:linear-gradient(160deg,#c9ccd2 0%,#7e848c 35%,#3e4249 65%,#9aa0a8 100%)}
.quote-box{position:absolute;left:52px;top:485px;width:1096px;height:156px;background:linear-gradient(90deg,#1c5a9e,#2f80c6 50%,#1c5a9e);border-radius:3px}
.quote-box h2{position:absolute;top:13px;width:100%;text-align:center;color:var(--white);font-size:19px;font-weight:500}
.field{position:absolute;height:32px;width:346px;background:var(--white);border-radius:3px;font-size:13px;color:#999;padding:8px 14px}
.send{position:absolute;left:855px;top:106px;width:117px;height:34px;background:var(--white);border-radius:3px;font-size:13px;font-weight:500;color:#222;text-align:center;line-height:34px}

/* intro */
.intro h2{position:absolute;top:702px;width:1200px;text-align:center;font-size:22px;font-weight:500;color:#222}
.intro .rule{position:absolute;left:53px;top:740px;width:1096px;border-top:2px dotted #d77a7a}
.intro p{position:absolute;left:53px;width:1096px;text-align:center;font-size:13px;color:var(--muted);line-height:21px}

/* feature grid */
.tile{position:absolute;width:600px;height:428px}
.tile.red{background:radial-gradient(circle at 45% 95%,var(--red-light),var(--red) 75%)}
.tile.blue{background:radial-gradient(circle at 50% 95%,var(--blue-light),#1a4f8f 75%)}
.tile.photo-white{background:linear-gradient(180deg,#c9d7e5 0%,#a7a39d 45%,#5a5d63 100%)}
.tile.photo-blue{background:linear-gradient(150deg,#dfe8f4 0%,#5b83b8 40%,#1d3d70 100%)}
.tile .copy{position:absolute;left:60px;right:60px;top:50%;transform:translateY(-50%);text-align:center;color:var(--white)}
.tile h3{font-size:27px;font-weight:500;margin-bottom:18px}
.tile p{font-size:15px;line-height:23px}

/* join band */
.join{position:absolute;left:0;top:1806px;width:1200px;height:161px;background:radial-gradient(ellipse at 50% 90%,var(--red-light),var(--red) 80%)}
.join h3{position:absolute;left:53px;top:50px;color:var(--white);font-size:28px;font-weight:700}
.join p{position:absolute;left:53px;top:92px;color:var(--white);font-size:15px}
.join .btn{position:absolute;left:1018px;top:69px;width:101px;height:47px;background:var(--navy);color:var(--white);font-size:13px;font-weight:500;text-align:center;line-height:47px;border-radius:2px}

/* footer */
.site-footer{position:absolute;left:0;top:1967px;width:1200px;height:456px;background:var(--navy);color:var(--white)}
.col{position:absolute;top:50px;font-size:13px;line-height:16px}
.col h4{font-size:18px;font-weight:500;margin-bottom:18px}
.col .row{margin-bottom:18px}
.col b{font-weight:500}
.col .about{font-size:13px;line-height:20px;margin-bottom:14px;width:250px}
.socials{display:flex;gap:16px;margin-top:4px}
.socials span{width:13px;height:13px;border-radius:50%;background:var(--white)}
.map{position:absolute;left:896px;top:92px;width:252px;height:213px;background:linear-gradient(135deg,#e9e4d8,#c9d9e6 55%,#e6dfd0);border:1px solid #ccc}
.foot-rule{position:absolute;left:53px;top:391px;width:1096px;border-top:1px solid #5a7099}
.copyright{position:absolute;top:418px;width:1200px;text-align:center;font-size:13px;font-weight:500}
</style>
</head>
<body>

<header class="site-header">
  <div class="nav-band"></div>
  <div class="utility">
    <span class="item">
      <svg width="12" height="12" viewBox="0 0 12 12"><path d="M2 1l2 0 1 3-1.5 1a6 6 0 0 0 3.5 3.5L8 7l3 1v2a1 1 0 0 1-1 1A9 9 0 0 1 1 2a1 1 0 0 1 1-1z" fill="#888"/></svg>
      +1-884-555-0142
    </span>
    <span class="item">
      <svg width="14" height="10" viewBox="0 0 14 10"><rect width="14" height="10" rx="1" fill="#888"/><path d="M0 1l7 5 7-5" stroke="#fff" fill="none"/></svg>
      Info@heronfreightways.net
    </span>
    <span class="pill driver">Become a Driver</span>
    <span class="pill quote">Get a Quote</span>
    <span class="pill login">Login</span>
  </div>
  <div class="logo-box"><span class="mark"></span><span class="name">Heron Freightways</span></div>
  <nav class="main-nav">
    <a href="#">HOME</a><a href="#">ABOUT US</a><a href="#">SERVICES</a><a href="#">RESOURCES</a><a href="#">CAREERS</a><a href="#">JOB</a><a href="#">CONTACT</a>
  </nav>
</header>

<div class="hero" role="img" aria-label="Blue semi truck with refrigerated trailer driving along a coastal highway beside crashing waves"></div>

<form class="quote-box">
  <h2>Quick Quote</h2>
  <div class="field" style="left:10px;top:55px">Location *</div>
  <div class="field" style="left:375px;top:55px">Destination *</div>
  <div class="field" style="left:740px;top:55px">Cargo / Personal</div>
  <div class="field" style="left:10px;top:106px">E-mail *</div>
  <div class="field" style="left:375px;top:106px">Contact Number *</div>
  <div class="send">SEND QUOTE</div>
</form>

<section class="intro">
  <h2>Transport Refrigeration Technology</h2>
  <div class="rule"></div>
  <p style="top:793px">We carry and deliver almost any type of temperature sensitive products anywhere in the United States.</p>
  <p style="top:834px">Heron Freightways, LLC currently has the very latest in transport refrigeration technology. Our brand new trucks and professional- looking equipment set the standard with outstanding efficiency and reliability paired with superior temperature control.</p>
  <p style="top:893px">We offer quality and reliability. We've got you and your business covered day and night, from origin to destination.</p>
</section>

<section class="features">
  <div class="tile red" style="left:0;top:951px">
    <div class="copy"><h3>Our Mission</h3><p>Our Mission is to provide our clients with safe, consistent and quality transportation solutions.</p></div>
  </div>
  <div class="tile photo-white" style="left:600px;top:951px" role="img" aria-label="White semi truck driving on a desert highway with mountains behind"></div>
  <div class="tile photo-blue" style="left:0;top:1378px" role="img" aria-label="Blue-toned truck speeding down a highway with motion blur"></div>
  <div class="tile blue" style="left:600px;top:1378px">
    <div class="copy"><h3>Our Logistics</h3><p>Team is committed to customer satisfaction, safety and trust. You can be sure your good will be delivered on time and in the best condition</p></div>
  </div>
</section>

<section class="join">
  <h3>Come join our Team!</h3>
  <p>We are now hiring CDL Truck Drivers 2 years min. experience required Apply in person or call 1-844-555-0142 or (956)555-0187</p>
  <div class="btn">JOIN NOW</div>
</section>

<footer class="site-footer">
  <div class="col" style="left:53px">
    <h4>Main Office</h4>
    <div class="row">Questions? Comments? Need a Quote?</div>
    <div class="row"><b>Phone:</b> +1-884-555-0142</div>
    <div class="row"><b>Local:</b> (956) 555 0187</div>
    <div class="row"><b>Office:</b> 1820 N. Mesquite Blvd. Calder, Tx 78590</div>
    <div class="row"><b>Support:</b> support@heronfreightways.net</div>
    <div class="socials"><span></span><span></span><span></span><span></span><span></span></div>
  </div>
  <div class="col" style="left:333px">
    <h4>General Manager</h4>
    <div class="row"><b>Name:</b> Mateo R. Salcedo</div>
    <div class="row"><b>Email:</b> mateosalcedo@heronfreightways.net</div>
    <h4>Office Manager/Accounting</h4>
    <div class="row"><b>Name:</b> Renata Ibarra</div>
    <div class="row"><b>Email:</b> renata@heronfreightways.net</div>
  </div>
  <div class="col" style="left:617px">
    <h4>About Team</h4>
    <p class="about">Enim congue blandit. Lorem ipsum dolor sit amet, consectetur adipiscing elit. Quisque consectetur interdum finibus. Vestibulum ante ipsum primis in faucibus orci. luctus et ultrices posuere.</p>
    <p class="about">Cubilia cras blandit finibus ipsum, id porttitor arcu volutpat a. Integer iaculis erat nec justo malesuada faucibus vel tempus sapien. Vivamus aliquam euismod tristique.</p>
  </div>
  <div class="col" style="left:896px"><h4>Headquarters in Map</h4></div>
  <div class="map" role="img" aria-label="Street map showing the headquarters location"></div>
  <div class="foot-rule"></div>
  <div class="copyright">Copyright 2016. All Rights Reserved by HeronFreightways</div>
</footer>

</body>
</html>
```